Brook Lending Flyer

Hi I need a professional flyer promoting me and my company. I can give you ideas of what to say once I see the design.

Below is my personal information needed in the flyer.

D: 510-437-2286
F: 877-540-6613
E: dean@BrookLendingInc.example
W: www.BrookLendingInc.example

NMLS# 475263/3081657 DRE# 02768419/03591864
Brook Lending Inc. | 127 Elm Avenue Ste. K | Pleasanton, CA 94583

Also I want to communicate tht we are friendly, fast, transparent, we communicate clearly and often, we educate (we want to make sure the buyer understands everything). Our team had over 60+ years experience. We are the alternative to the big box banks. We provide concierge service every step of the way.
Experience #The BrookLendingDifference

"Brook Lending is committed to a simple, fast, hassle free and fum mortgage experience every time." President -Dean Brook

Veteran Owned Business

Target Market(s)

Home buyers

Industry/Entity Type

Mortgage

Font styles to use
Decorative

Colors
59FF00
82FF00
B8FF75
E3FFCB
F4FFEA
FFC000
F8CF3A
FAE287
FDF2CF
FEFAEE

Requirements
Must have
• Please make it look professional maybe with some curves or something. Look at other really professional flyers for ideas.
Nice to have
• Curves and a couple areas to discuss why Brook Lending and types of financing we do
Should not have
• I don't know

```html
<!DOCTYPE html>
<html lang="en">
<head>
<meta charset="utf-8">
<title>Brook Lending Flyer</title>
<link rel="stylesheet" href="https://fonts.googleapis.com/css2?family=Marcellus&family=Arimo:wght@400&display=swap">
<style>
  :root {
    --ink: #0a0a0a;
    --paper: #ffffff;
    --gold: #f3c53c;
    --gold-band: #f2c744;
    --lime: #8def3f;
    --lime-band: #90f041;
    --leaf: #78b94a;
    --body-dark: #111111;
    --body-light: #ffffff;
  }
  * { margin: 0; padding: 0; box-sizing: border-box; }
  html, body { width: 1200px; height: 848px; overflow: hidden; background: var(--paper); }
  .flyer {
    position: relative;
    width: 1200px;
    height: 848px;
    overflow: hidden;
    background: var(--paper);
    font-family: "Arimo", Arial, sans-serif;
  }
  .backdrop { position: absolute; inset: 0; width: 1200px; height: 848px; }
  .photo-refinance {
    position: absolute;
    left: 828px; top: 0;
    width: 372px; height: 246px;
    background: linear-gradient(135deg, #cfd2d3 0%, #f2c84a 35%, #f4cd4f 65%, #c9c3b8 100%);
  }
  .photo-homes {
    position: absolute;
    left: 56px; top: 346px;
    width: 566px; height: 240px;
    background: linear-gradient(90deg, #e6cf7a 0%, #d9b848 45%, #dedfdf 72%, #eeeeee 100%);
    clip-path: polygon(79px 0, 221px 0, 221px 68px, 380px 68px, 380px 106px, 563px 106px, 563px 232px, 380px 232px, 380px 224px, 169px 224px, 169px 239px, 0 239px, 0 145px, 79px 145px);
  }
  .block { position: absolute; width: 340px; }
  .heading {
    font-family: "Marcellus", Georgia, serif;
    font-weight: 400;
    font-size: 24px;
    line-height: 1.1;
    color: var(--gold);
  }
  .heading--leaf { color: var(--leaf); }
  .copy {
    font-size: 12.8px;
    line-height: 17.1px;
    color: var(--body-light);
    margin-top: 5px;
    white-space: nowrap;
  }
  .copy--dark { color: var(--body-dark); }
  .service { position: absolute; width: 290px; }
  .service-number {
    width: 32px; height: 32px;
    border-radius: 50%;
    background: var(--lime);
    color: var(--ink);
    font-family: "Marcellus", Georgia, serif;
    font-size: 22px;
    line-height: 32px;
    text-align: center;
  }
  .service-title {
    font-family: "Marcellus", Georgia, serif;
    font-weight: 400;
    font-size: 18px;
    line-height: 1;
    margin-top: 9px;
    color: var(--gold);
  }
  .service-title--leaf { color: var(--leaf); }
  .service .copy { margin-top: 9px; }
  .call-to-action {
    position: absolute;
    left: 858px; top: 739px;
    font-family: "Marcellus", Georgia, serif;
    font-size: 24px;
    line-height: 29px;
    color: var(--body-light);
  }
  .call-to-action .phone { color: var(--gold); }
</style>
</head>
<body>
<main class="flyer">
  <div class="photo-refinance" role="img" aria-label="Photo of a yellow note reading Refinance beside an hourglass with a small house"></div>

  <svg class="backdrop" viewBox="0 0 1200 848" aria-hidden="true">
    <path d="M0 0 H847 C870 200 780 440 590 510 C390 580 140 480 0 236 Z" fill="var(--lime-band)"/>
    <path d="M0 0 H842 C862 196 772 432 584 500 C386 568 144 470 0 228 Z" fill="var(--gold-band)"/>
    <path d="M0 0 H832 C852 190 760 424 576 490 C380 556 148 460 0 218 Z" fill="var(--ink)"/>
    <path d="M700 848 C790 730 900 670 1010 670 C1080 670 1150 690 1200 712 V848 Z" fill="var(--lime-band)"/>
    <path d="M712 848 C800 742 906 684 1012 684 C1080 684 1150 704 1200 726 V848 Z" fill="var(--gold-band)"/>
    <path d="M726 848 C812 756 912 694 1014 694 C1080 694 1150 716 1200 738 V848 Z" fill="var(--ink)"/>
  </svg>

  <div class="photo-homes" role="img" aria-label="Illustration of model houses beside a calculator and stacks of gold coins"></div>

  <section class="block" style="left:49px; top:52px;">
    <h2 class="heading">Who We Are</h2>
    <p class="copy">In 1997 after serving 10 years in the US Navy as a<br>rescue swimmer and submarine hunter, Dean started<br>his career in the mortgage world. He has been<br>proudly helping his clients with their mortgage needs<br>ever since. He absolutely loves helping his clients<br>reach their financial goals.</p>
  </section>

  <section class="block" style="left:49px; top:199px;">
    <h2 class="heading">Our Work Speaks for Itself</h2>
    <p class="copy">95% of our business comes from repeat clients,<br>their referrals, real estate agents and other business<br>partners. They say they trust us ,and know we will get<br>the job done.</p>
  </section>

  <section class="block" style="left:440px; top:52px;">
    <h2 class="heading">Our Services</h2>
    <p class="copy">We offer a range of skilled mortgage and financial<br>services to help our clients achieve their financial<br>goals, including:</p>
  </section>

  <article class="service" style="left:440px; top:150px;">
    <div class="service-number">1</div>
    <h3 class="service-title">Refinancing</h3>
    <p class="copy">Lorem ipsum lorem ipsum lorem ipsum lorwm<br>ipsum lorem ipsum lorem ipsum lorem ipsum<br>lorem ipsum lorem ipsum.</p>
  </article>

  <article class="service" style="left:440px; top:282px;">
    <div class="service-number">2</div>
    <h3 class="service-title">Mortgages</h3>
    <p class="copy">Lorem ipsum lorem ipsum lorem ipsum lorwm<br>ipsum lorem ipsum lorem ipsum lorem ipsum<br>lorem ipsum lorem ipsum.</p>
  </article>

  <article class="service" style="left:440px; top:617px;">
    <div class="service-number">3</div>
    <h3 class="service-title service-title--leaf">Service Item</h3>
    <p class="copy copy--dark">Lorem ipsum lorem ipsum lorem ipsum lorwm<br>ipsum lorem ipsum lorem ipsum lorem ipsum<br>lorem ipsum lorem ipsum.</p>
  </article>

  <article class="service" style="left:842px; top:272px;">
    <div class="service-number">4</div>
    <h3 class="service-title service-title--leaf">Service Item</h3>
    <p class="copy copy--dark">Lorem ipsum lorem ipsum lorem ipsum lorwm<br>ipsum lorem ipsum lorem ipsum lorem ipsum<br>lorem ipsum lorem ipsum.</p>
  </article>

  <article class="service" style="left:844px; top:404px;">
    <div class="service-number">5</div>
    <h3 class="service-title service-title--leaf">Service Item</h3>
    <p class="copy copy--dark">Lorem ipsum lorem ipsum lorem ipsum lorwm<br>ipsum lorem ipsum lorem ipsum lorem ipsum<br>lorem ipsum lorem ipsum.</p>
  </article>

  <article class="service" style="left:844px; top:536px;">
    <div class="service-number">6</div>
    <h3 class="service-title service-title--leaf">Service Item</h3>
    <p class="copy copy--dark">Lorem ipsum lorem ipsum lorem ipsum lorwm<br>ipsum lorem ipsum lorem ipsum lorem ipsum<br>lorem ipsum lorem ipsum.</p>
  </article>

  <section class="block" style="left:54px; top:620px;">
    <h2 class="heading heading--leaf">What We Do Best</h2>
    <p class="copy copy--dark">Our job is to understand your overall financial<br>position and then provide the best advice as to how<br>you can reach your financial goals. Our approach<br>is honest, straightforward advice in a confidential<br>private environment. We educate our clients on the<br>entire process so we eliminate their fears and create<br>confidence going forward to a more comfortable<br>environment.</p>
  </section>

  <p class="call-to-action">Reach out to Dean today by<br>calling <span class="phone">510-437-2286!</span></p>
</main>
</body>
</html>
```